Vorn Lux

Hello - our company Brightfen 4 develops novel products for the skin, & hair care industry as well as dietary supplements. We're looking for a label design for a new product. The product is a premium hair loss/growth supplement. Our primary demo is women ages 45-65. I attached the brand logo & some competitive product designs that we find attractive.

I've been traveling & have not had the time to adequately review the designs, please be patient with me.

```html
<!DOCTYPE html>
<html lang="en">
<head>
<meta charset="utf-8">
<title>Vorn Lux – Advance Formula Women Label</title>
<link rel="stylesheet" href="https://fonts.googleapis.com/css2?family=Exo+2:wght@300;400;800;900&family=Montserrat:wght@400;600;700&display=swap">
<style>
  :root {
    --backdrop: #727272;
    --label-white: #ffffff;
    --ink-dark: #454545;
    --ink-mid: #6a6a6a;
    --ink-black: #2b2b2b;
    --brand-blue: #4ea6dc;
    --band-deep: #1769ad;
    --band-light: #57b0e5;
    --panel-deep: #1a6db0;
    --panel-edge: #3d92cf;
    --chevron-light: #d9dde2;
    --aloe-light: #8cc63f;
    --aloe-dark: #2f7a22;
  }
  * { margin: 0; padding: 0; box-sizing: border-box; }
  html, body {
    width: 1200px;
    height: 2526px;
    overflow: hidden;
    background: var(--backdrop);
  }
  .label {
    position: absolute;
    left: 167px;
    top: 934px;
    width: 866px;
    height: 658px;
    background: var(--label-white);
    overflow: hidden;
    box-shadow: 0 30px 40px rgba(0,0,0,0.35);
  }
  .text-line {
    position: absolute;
    left: 0;
    width: 100%;
    text-align: center;
    white-space: nowrap;
  }
  .product-line {
    top: 22px;
    font-family: "Exo 2", sans-serif;
    font-weight: 300;
    font-size: 58px;
    line-height: 64px;
    color: var(--ink-dark);
    letter-spacing: 1px;
  }
  .claim {
    top: 84px;
    font-family: "Montserrat", sans-serif;
    font-weight: 700;
    font-size: 16px;
    line-height: 20px;
    letter-spacing: 2.5px;
    color: var(--ink-mid);
  }
  .extract {
    top: 104px;
    font-family: "Montserrat", sans-serif;
    font-weight: 400;
    font-size: 15px;
    line-height: 20px;
    color: var(--ink-black);
  }
  .aloe-art {
    position: absolute;
    left: 345px;
    top: 132px;
    width: 176px;
    height: 184px;
    border-radius: 50% 50% 46% 46% / 30% 30% 70% 70%;
    background: radial-gradient(ellipse at 50% 80%, var(--aloe-dark), var(--aloe-light) 75%, transparent 76%);
  }
  .brand-name {
    top: 330px;
    font-family: "Exo 2", sans-serif;
    font-weight: 400;
    font-size: 72px;
    line-height: 80px;
    color: var(--brand-blue);
    letter-spacing: 3px;
  }
  .strength {
    top: 408px;
    font-family: "Exo 2", sans-serif;
    font-weight: 400;
    font-size: 25px;
    line-height: 30px;
    letter-spacing: 4px;
    color: var(--ink-black);
  }
  .band {
    position: absolute;
    left: 0;
    top: 442px;
    width: 866px;
    height: 216px;
  }
  .formula {
    top: 456px;
    font-family: "Exo 2", sans-serif;
    font-weight: 400;
    font-size: 40px;
    line-height: 44px;
    letter-spacing: 1px;
    color: var(--label-white);
  }
  .audience {
    top: 496px;
    font-family: "Exo 2", sans-serif;
    font-weight: 900;
    font-size: 42px;
    line-height: 46px;
    letter-spacing: 1px;
    color: var(--label-white);
  }
  .tagline {
    top: 604px;
    font-family: "Montserrat", sans-serif;
    font-weight: 400;
    font-size: 15px;
    line-height: 18px;
    color: var(--label-white);
  }
  .tagline-strong {
    top: 622px;
    font-family: "Montserrat", sans-serif;
    font-weight: 600;
    font-size: 16px;
    line-height: 18px;
    color: var(--label-white);
  }
</style>
</head>
<body>
  <main class="label">
    <div class="text-line product-line">Brightfen 4</div>
    <div class="text-line claim">MEDICALLY PROVEN</div>
    <div class="text-line extract">He Shuld 12:1 Extract</div>
    <div class="aloe-art" role="img" aria-label="Illustration of a green aloe vera plant"></div>
    <div class="text-line brand-name">Vorn Lux</div>
    <div class="text-line strength">CLINICAL STRENGTH</div>

    <svg class="band" viewBox="0 0 866 216" aria-hidden="true">
      <defs>
        <linearGradient id="panelGrad" x1="0" y1="0" x2="1" y2="0">
          <stop offset="0" stop-color="var(--panel-edge)"/>
          <stop offset="0.5" stop-color="var(--panel-deep)"/>
          <stop offset="1" stop-color="var(--panel-edge)"/>
        </linearGradient>
        <linearGradient id="chevronGrad" x1="0" y1="0" x2="1" y2="0">
          <stop offset="0" stop-color="var(--band-light)"/>
          <stop offset="0.5" stop-color="var(--chevron-light)"/>
          <stop offset="1" stop-color="var(--band-light)"/>
        </linearGradient>
      </defs>
      <rect x="0" y="0" width="866" height="216" fill="var(--band-light)"/>
      <rect x="0" y="0" width="866" height="41" fill="var(--band-deep)"/>
      <polygon points="180,94 433,150 686,94 686,106 433,164 180,106" fill="url(#chevronGrad)"/>
      <polygon points="180,0 686,0 686,94 433,150 180,94" fill="url(#panelGrad)"/>
    </svg>

    <div class="text-line formula">Advance Formula</div>
    <div class="text-line audience">WOMEN</div>
    <div class="text-line tagline">Product Is A Premium</div>
    <div class="text-line tagline-strong">Hair Loss/growth Supplement</div>
  </main>
</body>
</html>
```